Beauty spa price list booklet. 16 pages from front to rear. Mainly white with compay logo

I need an A6 sized booklet for a beauty day spa.To incorporate our company logo, stock beauty photos (massages, facials, will send some examples over shortly.)16 Pages from front to rear.

Text sent over to be incorporated into the design as similar as the example one I've sent your as you can. Uploaded stock photos to be used in the correct places (Ie waxing photo on the waxing page etc....)

I've sent over a lot of the menu text but:

***I WILL WRITE UP AND SEND OVER THE REST OF THE LUMARA SPA TREATMENT TEXT IN THE NEXT DAY OR TWO!!***

Target Market(s)

Customers using the spa. to take it away and keep at home.

Font styles to use
Serif
Sans Serif

Colors
00a990
33a6d7
ffffff

Requirements
Must have
• Company logo. Price lists.
• We like the use of white (for the most part. And teal tones in places.)
• Clear professional text with a good layout.

```html
<!DOCTYPE html>
<html lang="en">
<head>
<meta charset="utf-8">
<title>About – Lumara House Day Spa</title>
<link rel="stylesheet" href="https://fonts.googleapis.com/css2?family=Allura&family=Crimson+Text&display=swap">
<style>
  :root {
    --paper: #ffffff;
    --ink-script: #2f5a80;
    --panel: rgba(84, 109, 143, 0.92);
    --text-light: #ffffff;
    --wash-deep: #7e93ad;
    --wash-mid: #a8b7c9;
    --wash-pale: #dfe5ec;
  }
  * { margin: 0; padding: 0; box-sizing: border-box; }
  html, body { width: 848px; height: 1200px; overflow: hidden; background: var(--paper); }
  .page {
    position: relative;
    width: 848px;
    height: 1200px;
    background: var(--paper);
    overflow: hidden;
  }
  .wash {
    position: absolute;
  }
  .wash--top-right { left: 500px; top: 0; width: 348px; height: 400px; }
  .wash--bottom-left { left: 0; top: 800px; width: 270px; height: 400px; }
  .page-title {
    position: absolute;
    left: 0;
    width: 848px;
    top: 82px;
    text-align: center;
    font-family: "Allura", cursive;
    font-weight: 400;
    font-size: 128px;
    line-height: 1;
    color: var(--ink-script);
  }
  .about-panel {
    position: absolute;
    left: 70px;
    top: 248px;
    width: 708px;
    height: 802px;
    background: var(--panel);
    padding: 307px 9px 0;
    padding-top: 59px;
    text-align: center;
    color: var(--text-light);
    font-family: "Crimson Text", serif;
    font-size: 30.5px;
    line-height: 69px;
  }
  .about-panel p + p { margin-top: 69px; }
</style>
</head>
<body>
  <main class="page">
    <svg class="wash wash--top-right" viewBox="0 0 348 400" role="img" aria-label="Soft blue watercolour wash decoration">
      <defs>
        <radialGradient id="washTop" cx="0.6" cy="0.35" r="0.65">
          <stop offset="0" stop-color="var(--wash-deep)" stop-opacity="0.85"/>
          <stop offset="0.55" stop-color="var(--wash-mid)" stop-opacity="0.6"/>
          <stop offset="1" stop-color="var(--wash-pale)" stop-opacity="0"/>
        </radialGradient>
      </defs>
      <ellipse cx="210" cy="170" rx="200" ry="230" fill="url(#washTop)"/>
    </svg>
    <svg class="wash wash--bottom-left" viewBox="0 0 270 400" role="img" aria-label="Soft blue watercolour wash decoration">
      <defs>
        <radialGradient id="washBottom" cx="0.3" cy="0.6" r="0.65">
          <stop offset="0" stop-color="var(--wash-deep)" stop-opacity="0.85"/>
          <stop offset="0.55" stop-color="var(--wash-mid)" stop-opacity="0.6"/>
          <stop offset="1" stop-color="var(--wash-pale)" stop-opacity="0"/>
        </radialGradient>
      </defs>
      <ellipse cx="90" cy="230" rx="190" ry="220" fill="url(#washBottom)"/>
    </svg>

    <h1 class="page-title">About</h1>

    <section class="about-panel">
      <p>Welcome to Lumara House Day Spa. We are situated in the heart of the beautiful seaside town of Wavecliff in East Sussex. Conveniently placed for access to nearby bars and restaurants, the beach is only a short walk away.</p>
      <p>Lumara House Day Spa invites you to relax and unwind in our peaceful setting, let us pamper you and restore your feelings of calm and wellness.</p>
    </section>
  </main>
</body>
</html>
```